Poster for Display Sign - Pet Related

Looking for a poster for my brochure display rack. The display rack will be taken to trade shows and the sign should catch attention of our audience as they pass by.
The poster frame size is 24" x 36". The view able area is 23" x 35".
We are a pet product delivery service for our local community. The sign should communicate trust and be personable and inviting.
The final design should also be sent in a format that can be printed to any size.
You can visit our website at: www.BrightWhiskerRuns.com to get a feel for our company.
Target Market(s)
Higher than average households looking to make their lives easier by having their pet products delivered to their door.
Industry/Entity Type
Delivery Service
Requirements
Must have
- Logo, image of dogs/cats/person with their pet, web address: www.BrightWhiskerRuns.com, phone number: 920-386-2751.
Can play around with the text of either: Sit. Stay. Let us Fetch! Or, making your life easier, theirs healthier and happier.
Nice to have
- Use of our colors: orange, blue and green.
If space allows, can contain the text: Owning a pet is an amazing experience, but there is no denying that one of the least enjoyable aspects of pet ownership is driving to the store to buy pet food. Getting premium pet products delivered right to your door has never been easier. At Bright Whisker, we strive to make one of the most inconvenient parts of pet ownership as hassle and worry free as possible.
Should not have
- Delivery trucks/cars, lots of random paw prints.

```html
<!DOCTYPE html>
<html lang="en">
<head>
<meta charset="utf-8">
<title>Bright Whisker – Display Poster</title>
<link rel="stylesheet" href="https://fonts.googleapis.com/css2?family=Questrial&family=Arimo:wght@400&display=swap">
<style>
  :root {
    --backdrop: #000000;
    --paper: #ffffff;
    --brand-blue: #3aa8df;
    --brand-green: #9bc63c;
    --brand-orange: #f0921f;
    --ink-grey: #5f5f5f;
    --logo-grey: #6b6b6b;
    --tagline-grey: #8a8a8a;
    --dot-dark: #333333;
  }
  * { margin: 0; padding: 0; box-sizing: border-box; }
  html, body {
    width: 1000px;
    height: 1200px;
    overflow: hidden;
    background: var(--backdrop);
  }
  .poster {
    position: absolute;
    left: 148px;
    top: 50px;
    width: 704px;
    height: 1103px;
    background: var(--paper);
    overflow: hidden;
  }
  .brand {
    position: absolute;
    left: 50px;
    top: 178px;
    font-family: "Questrial", sans-serif;
  }
  .brand-name {
    display: flex;
    align-items: center;
    gap: 12px;
    font-size: 50px;
    line-height: 1;
    color: var(--logo-grey);
  }
  .brand-dot {
    width: 22px;
    height: 22px;
    border-radius: 50%;
    background: var(--brand-orange);
    flex: none;
  }
  .brand-tagline {
    margin-top: 18px;
    font-size: 12.5px;
    letter-spacing: 0.6px;
    color: var(--tagline-grey);
  }
  .contact {
    position: absolute;
    right: 27px;
    top: 42px;
    text-align: right;
    font-family: "Arimo", sans-serif;
    font-style: normal;
    font-size: 24px;
    line-height: 41px;
    letter-spacing: -0.3px;
    color: var(--ink-grey);
  }
  .cat-art {
    position: absolute;
    left: 360px;
    top: 150px;
    width: 330px;
    height: 890px;
    border-radius: 160px 160px 60px 60px;
    background: linear-gradient(180deg,
      rgba(58,168,223,0.16) 0%,
      rgba(155,198,60,0.12) 50%,
      rgba(240,146,31,0.16) 100%);
  }
  .intro-panel {
    position: absolute;
    left: 204px;
    top: 535px;
    width: 340px;
    height: 465px;
  }
  .intro-text {
    position: absolute;
    left: 215px;
    top: 628px;
    width: 300px;
    font-family: "Arimo", sans-serif;
    font-size: 14.5px;
    line-height: 23px;
    color: var(--paper);
    text-align: center;
  }
  .headline {
    position: absolute;
    left: 0;
    top: 0;
    width: 704px;
    height: 1103px;
    font-family: "Questrial", sans-serif;
    font-size: 52px;
  }
  .headline .blue { fill: var(--brand-blue); }
  .headline .green { fill: var(--brand-green); }
  .headline .orange { fill: var(--brand-orange); }
  .headline .dark { fill: var(--dot-dark); }
</style>
</head>
<body>
  <main class="poster">
    <header class="brand">
      <div class="brand-name"><span class="brand-dot"></span>Bright Whisker</div>
      <div class="brand-tagline">PREMIUM PET PRODUCTS DELIVERED</div>
    </header>

    <address class="contact">
      <div>BrightWhiskerRuns.com</div>
      <div>Phone-920-386-2751</div>
    </address>

    <div class="cat-art" role="img" aria-label="Line-art illustration of a seated cat drawn in blue, orange and green strokes"></div>

    <svg class="intro-panel" viewBox="0 0 340 465" aria-hidden="true">
      <path d="M110,28 C170,-5 260,0 305,35 C345,70 330,140 300,195 C275,240 300,300 318,360 C335,420 295,462 205,464 C125,466 30,458 8,400 C-10,345 18,290 38,240 C58,190 40,145 52,100 C62,65 80,42 110,28 Z" fill="var(--brand-blue)"/>
    </svg>

    <p class="intro-text">Owning a pet is an<br>amazing experience,<br>but there is no denying that<br>one of the least enjoyable aspects<br>of pet ownership is driving to the<br>store to buy pet food. Getting<br>premium pet products delivered<br>right to your door has never been<br>easier. At Bright Whisker, we strive<br>to make one of the most inconvenient<br>parts of pet ownership as<br>hassle and worry free as<br>possible.</p>

    <svg class="headline" viewBox="0 0 704 1103">
      <defs>
        <path id="arc-one" d="M48,812 Q60,560 352,325"/>
        <path id="arc-two" d="M105,968 Q100,625 335,382"/>
        <path id="arc-three" d="M165,1038 Q160,730 312,492"/>
      </defs>
      <text><textPath href="#arc-one" class="blue" textLength="600" lengthAdjust="spacingAndGlyphs">Sit. Stay. Let us Fetch !</textPath></text>
      <text><textPath href="#arc-two" class="green" textLength="640" lengthAdjust="spacingAndGlyphs">Or, making your life easier,</textPath></text>
      <text><textPath href="#arc-three" class="orange" textLength="575" lengthAdjust="spacingAndGlyphs">theirs healthier and happier<tspan class="dark">.</tspan></textPath></text>
    </svg>
  </main>
</body>
</html>
```